Redesign current website

Current website www.tarnvalepropertyco.com.au needs to be redone.

Content will be the same however the visual look needs to be upgraded.

Need ability to WYSIWYG editor any of the pages, including embedding videos and images throughout the pages.

It currently looks dated and a bit dodgy. Need the same functionality (i.e. submission forms etc...) however need it to look much more modern.

Needs to be easy to navigate, and look fresh, credible and professional.

Must be mobile compatible and SEO friendly.

Not interested in sites that look like the 1000+ one websites templates.

```html
<!DOCTYPE html>
<html lang="en">
<head>
<meta charset="utf-8">
<title>Tarnvale Property Co</title>
<link rel="stylesheet" href="https://fonts.googleapis.com/css2?family=Roboto:wght@300;400;500;700&family=Raleway:wght@400;500&family=Oswald:wght@400;500;700&display=swap">
<style>
:root{
  --blue:#2356c4;
  --blue-dark:#1a3f98;
  --blue-nav:#2a60cf;
  --footer:#1f47a5;
  --footer-bar:#1a3a8a;
  --gold:#d4a23a;
  --orange:#f39322;
  --ink:#333;
  --muted:#666;
  --soft:#f5f5f5;
}
*{margin:0;padding:0;box-sizing:border-box}
html,body{width:1200px;height:2410px;overflow:hidden;background:#fff;font-family:"Roboto",sans-serif;color:var(--ink)}
.page{position:relative;width:1200px;height:2410px}
.abs{position:absolute}
.brand{left:0;top:0;width:1200px;height:137px;display:flex;align-items:center;justify-content:center;gap:14px}
.brand-mark{width:30px;height:30px;background:var(--blue)}
.brand-name{font-family:"Roboto",sans-serif;font-weight:700;font-size:38px;color:var(--blue)}
.nav{left:0;top:137px;width:1200px;height:57px;background:linear-gradient(#2f67d6,#2152bd)}
.nav-home{left:100px;top:0;width:80px;height:57px;background:var(--gold);display:flex;align-items:center;justify-content:center}
.nav-link{top:0;line-height:57px;font-size:13px;color:#fff;letter-spacing:.2px}
.hero{left:0;top:194px;width:1200px;height:529px;background:linear-gradient(180deg,#8fb3de 0%,#c9dcef 35%,#9aa79a 55%,#5e8a3a 78%,#77a94a 100%)}
.hero-title{left:842px;top:375px;font-family:"Oswald",sans-serif;font-weight:700;font-size:88px;line-height:1;color:#fff}
.hero-sub{left:842px;top:480px;font-family:"Oswald",sans-serif;font-weight:500;font-size:40px;line-height:1;color:#fff}
.hero-text{left:842px;top:540px;width:270px;font-size:14px;line-height:21px;color:#fff}
.hero-arrow{top:636px;width:29px;height:29px;border-radius:50%;background:#333;display:flex;align-items:center;justify-content:center}
.welcome{left:0;top:760px;width:1200px;text-align:center;font-family:"Raleway",sans-serif;font-size:32px;color:#333}
.welcome span{color:#666}
.welcome-copy{left:125px;top:814px;width:951px;text-align:center;font-size:12.5px;line-height:21px;color:var(--muted)}
.feature-icon{top:945px;width:104px;height:104px;border-radius:50%;background:var(--blue);border:4px solid #c9d7f3;display:flex;align-items:center;justify-content:center}
.feature-kicker{font-size:14px;color:#333}
.feature-title{font-size:26px;color:var(--blue-dark);margin-top:4px}
.feature-copy{font-size:12px;line-height:19px;color:var(--muted);margin-top:8px}
.divider{top:925px;width:1px;height:140px;background:#e6e6e6}
.listings{left:0;top:1118px;width:1200px;height:456px;background:var(--soft)}
.section-title{font-size:22px;color:#222}
.square-arrow{top:1151px;width:29px;height:29px;background:#2b2b2b;display:flex;align-items:center;justify-content:center;border-radius:3px}
.card{top:1204px;width:229px}
.card-photo{width:229px;height:178px}
.card-title{font-size:16px;color:#333;margin-top:18px}
.card-copy{font-size:11.5px;line-height:21px;color:var(--muted);margin-top:6px}
.btn-light{display:inline-block;background:linear-gradient(#fff,#ececec);border:1px solid #dcdcdc;box-shadow:0 2px 3px rgba(0,0,0,.12);color:var(--blue-dark);font-size:12px;font-weight:500;text-align:center}
.card .btn-light{width:129px;height:35px;line-height:33px;margin-top:18px}
.video-title{left:101px;top:1624px;font-size:25px;color:var(--blue)}
.lender-title{left:544px;top:1628px;font-size:21px;color:#333}
.post-title{left:241px;top:1924px;font-size:15px;color:#444}
.post-date{left:241px;top:1951px;font-size:13px;color:var(--orange)}
.post-copy{left:241px;top:1977px;width:220px;font-size:11.5px;line-height:19px;color:var(--muted)}
.contact-icon{left:545px;width:48px;height:48px;border-radius:50%;background:#f1f1f1;display:flex;align-items:center;justify-content:center}
.contact-text{left:610px;font-size:13px;line-height:21px;color:#555}
.lender-copy{left:853px;width:250px;font-size:11.5px;line-height:20.5px;color:var(--muted)}
.footer{left:0;top:2081px;width:1200px;height:267px;background:var(--footer)}
.footer-bar{left:0;top:2348px;width:1200px;height:62px;background:var(--footer-bar);text-align:center;line-height:62px;font-size:11px;color:#fff}
.footer-head{top:2122px;font-size:15px;color:#fff}
.footer-list{top:2163px;list-style:none;font-size:12px;line-height:24px;color:#fff}
.news-copy{left:546px;top:2155px;width:240px;font-size:11px;line-height:18px;color:#fff}
.news-input{left:546px;top:2205px;width:225px;height:40px;background:#fff;font-size:11px;line-height:40px;padding-left:14px;color:#333}
.news-btn{left:546px;top:2258px;width:90px;height:34px;background:var(--orange);color:#fff;font-size:11px;line-height:34px;text-align:center}
.footer-contact{left:850px;top:2152px;font-size:12px;line-height:20px;color:#fff}
.footer-row{left:850px;font-size:13px;color:#fff;display:flex;align-items:center;gap:14px}
.social{top:2279px;width:23px;height:23px;border-radius:50%;border:1.5px solid #fff}
</style>
</head>
<body>
<div class="page">

  <header class="abs brand"><span class="brand-mark"></span><span class="brand-name">Tarnvale Property Co</span></header>

  <nav class="abs nav">
    <div class="abs nav-home"><svg width="24" height="22" viewBox="0 0 24 22"><path d="M12 2 1 12h3v9h6v-6h4v6h6v-9h3z" fill="#fff"/></svg></div>
    <span class="abs nav-link" style="left:214px">ABOUT TARNVALE</span>
    <span class="abs nav-link" style="left:379px">OUR SOLUTIONS</span>
    <span class="abs nav-link" style="left:556px">HOW IT WORKS</span>
    <span class="abs nav-link" style="left:729px">PRIVATE LENDER ALERT</span>
    <span class="abs nav-link" style="left:957px">CONTACT US</span>
  </nav>

  <section class="abs hero" role="img" aria-label="Suburban two-storey houses with green lawns under a blue sky"></section>
  <div class="abs hero-title">Tarnvale</div>
  <div class="abs hero-sub">PROPERTY CO</div>
  <p class="abs hero-text">Sed bibendum, arcu ac rhoncus adipiscing, nulla lectus dictum mauris, non volutpat massa ipsum</p>
  <div class="abs hero-arrow" style="left:841px"><svg width="10" height="12"><path d="M8 1 3 6l5 5" stroke="#fff" stroke-width="2" fill="none"/></svg></div>
  <div class="abs hero-arrow" style="left:877px"><svg width="10" height="12"><path d="M2 1l5 5-5 5" stroke="#fff" stroke-width="2" fill="none"/></svg></div>

  <h1 class="abs welcome" style="font-weight:400">Welcome To <span>Tarnvale Property Co</span></h1>
  <p class="abs welcome-copy">Lorem ipsum dolor sit amet, consectetur adipiscing elit, sed do eiusmod tempor incididunt ut labore et dolore magna aliqua. Ut enim ad minim veniam, quis nostrud exercitation ullamco laboris nisi ut aliquip ex ea commodo consequat. Duis aute irure dolor in reprehenderit in voluptate velit esse cillum dolore eu fugiat nulla pariatur. Excepteur sint occaecat cupidatat non proident, sunt in culpa qui officia deserunt mollit anim id est laborum</p>

  <div class="abs feature-icon" style="left:103px"><svg width="48" height="46" viewBox="0 0 48 46"><path d="M24 3 3 21h6v22h30V21h6z" fill="#fff"/><rect x="15" y="24" width="7" height="7" fill="#2356c4"/><rect x="26" y="24" width="7" height="7" fill="#2356c4"/><rect x="20" y="34" width="8" height="9" fill="#2356c4"/></svg></div>
  <div class="abs" style="left:226px;top:958px;width:190px"><div class="feature-kicker">PROPERTIES FOR</div><div class="feature-title">RESIDENTIAL</div><div class="feature-copy">Sed ut perspiciatis unde omnis iste natus error sit voluptatem</div></div>
  <div class="abs divider" style="left:430px"></div>
  <div class="abs feature-icon" style="left:467px"><svg width="50" height="48" viewBox="0 0 50 48"><rect x="6" y="14" width="16" height="32" fill="#fff"/><rect x="24" y="4" width="20" height="42" fill="#fff"/><g fill="#2356c4"><rect x="10" y="19" width="3" height="4"/><rect x="15" y="19" width="3" height="4"/><rect x="10" y="27" width="3" height="4"/><rect x="15" y="27" width="3" height="4"/><rect x="28" y="10" width="4" height="4"/><rect x="36" y="10" width="4" height="4"/><rect x="28" y="19" width="4" height="4"/><rect x="36" y="19" width="4" height="4"/><rect x="28" y="28" width="4" height="4"/><rect x="36" y="28" width="4" height="4"/></g></svg></div>
  <div class="abs" style="left:591px;top:958px;width:175px"><div class="feature-kicker">APARTMENTS FOR</div><div class="feature-title">COMMERCIAL</div><div class="feature-copy">Sed ut perspiciatis unde omnis iste natus error sit volupt</div></div>
  <div class="abs divider" style="left:784px"></div>
  <div class="abs feature-icon" style="left:817px"><svg width="46" height="34" viewBox="0 0 46 34"><rect x="2" y="2" width="42" height="30" rx="3" fill="none" stroke="#fff" stroke-width="3.5"/><path d="M3 4l20 15L43 4" fill="none" stroke="#fff" stroke-width="3.5"/></svg></div>
  <div class="abs" style="left:936px;top:958px;width:175px"><div class="feature-kicker">REQUEST AN ESTIMATE</div><div class="feature-copy" style="margin-top:12px">Sed ut perspiciatis unde omnis iste natus error sit volu Sed ut perspiciatis unde omnis</div></div>

  <section class="abs listings"></section>
  <h2 class="abs section-title" style="left:100px;top:1152px;font-weight:400">LATEST ADDED PROPERTIES</h2>
  <div class="abs square-arrow" style="left:1039px"><svg width="8" height="12"><path d="M7 1 2 6l5 5" stroke="#fff" stroke-width="2" fill="none"/></svg></div>
  <div class="abs square-arrow" style="left:1073px"><svg width="8" height="12"><path d="M1 1l5 5-5 5" stroke="#fff" stroke-width="2" fill="none"/></svg></div>

  <article class="abs card" style="left:103px"><div class="card-photo" role="img" aria-label="White two-storey house with grey roof and front lawn" style="background:linear-gradient(#7fb0d8 0%,#b8cfe0 45%,#6b7a78 62%,#5f9a34 100%)"></div><div class="card-title">Sed docendi copiosae</div><div class="card-copy">Lorem ipsum dolor sit amet, consectetur scing elit, sed do eiusmod tempor Lorem ipsum dolor sit amet.</div><span class="btn-light">VIEW PROPERTY</span></article>
  <article class="abs card" style="left:360px"><div class="card-photo" role="img" aria-label="Beige brick family home with double garage under a blue sky" style="background:linear-gradient(#2f6fc4 0%,#5c8fd0 40%,#a89278 60%,#4d7a2a 100%)"></div><div class="card-title">Sed docendi copiosae</div><div class="card-copy">Lorem ipsum dolor sit amet, consectetur scing elit, sed do eiusmod tempor Lorem ipsum dolor sit amet.</div><span class="btn-light">VIEW PROPERTY</span></article>
  <article class="abs card" style="left:617px"><div class="card-photo" role="img" aria-label="Large green Victorian-style mansion with turret" style="background:linear-gradient(#3b79c9 0%,#76a3d8 40%,#7f9583 62%,#a3a39a 100%)"></div><div class="card-title">Sed docendi copiosae</div><div class="card-copy">Lorem ipsum dolor sit amet, consectetur scing elit, sed do eiusmod tempor Lorem ipsum dolor sit amet.</div><span class="btn-light">VIEW PROPERTY</span></article>
  <article class="abs card" style="left:874px"><div class="card-photo" role="img" aria-label="Red brick house with landscaped garden and lawn" style="background:linear-gradient(#2565c0 0%,#5a8fd2 40%,#9a5a48 60%,#52a02e 100%)"></div><div class="card-title">Sed docendi copiosae</div><div class="card-copy">Lorem ipsum dolor sit amet, consectetur scing elit, sed do eiusmod tempor Lorem ipsum dolor sit amet.</div><span class="btn-light">VIEW PROPERTY</span></article>

  <h2 class="abs video-title" style="font-weight:400">Our Latest Video</h2>
  <div class="abs" role="img" aria-label="Video still of a family standing in front of their new home" style="left:101px;top:1673px;width:384px;height:225px;background:linear-gradient(#b9c2c9 0%,#9a958c 45%,#6d7d55 75%,#5c8a38 100%)"></div>
  <svg class="abs" style="left:268px;top:1760px" width="52" height="52" viewBox="0 0 52 52"><circle cx="26" cy="26" r="25" fill="rgba(255,255,255,.55)"/><path d="M21 16v20l16-10z" fill="#fff"/></svg>
  <div class="abs" role="img" aria-label="Resort with pool and palm trees" style="left:101px;top:1922px;width:124px;height:92px;background:linear-gradient(#6f8f6a,#3f8fb0 70%,#7c6b52)"></div>
  <div class="abs post-title">Mes cuml dia sed in lacus</div>
  <div class="abs post-date">JAN 13, 2015</div>
  <p class="abs post-copy">Morbi tempor quam vel massa adi scing ute cursus mi congue pelle ntesque</p>

  <h2 class="abs lender-title" style="font-weight:400">PRIVATE LENDER ALERT</h2>
  <div class="abs" role="img" aria-label="Smiling professional woman at an office desk" style="left:546px;top:1678px;width:284px;height:172px;background:linear-gradient(90deg,#5a5f66 0%,#c7ccd2 30%,#e8ecf0 60%,#a7c08a 100%)"></div>
  <div class="abs contact-icon" style="top:1873px"><svg width="20" height="18" viewBox="0 0 24 22"><path d="M12 2 1 12h3v9h6v-6h4v6h6v-9h3z" fill="#333"/></svg></div>
  <div class="abs contact-text" style="top:1872px">42 Tarnvale Street, 2nd<br>Floor Napa, CA 94512</div>
  <div class="abs contact-icon" style="top:1951px"><svg width="20" height="20" viewBox="0 0 24 24"><path d="M6.6 10.8a15.1 15.1 0 0 0 6.6 6.6l2.2-2.2c.3-.3.7-.4 1-.2 1.1.4 2.3.6 3.6.6.6 0 1 .4 1 1V20c0 .6-.4 1-1 1A17 17 0 0 1 3 4c0-.6.4-1 1-1h3.5c.6 0 1 .4 1 1 0 1.3.2 2.5.6 3.6.1.3 0 .7-.2 1z" fill="#333"/></svg></div>
  <div class="abs contact-text" style="top:1950px">Phone No : +1800 555 318<br>info@tarnvalepropertyco.com.au</div>
  <p class="abs lender-copy" style="top:1673px">Lorem ipsum dolor sit amet, consectetur adipiscing elit, sed do eiusmod tempor incididunt ut labore et dolore magna aliqua. Ut enim ad minim veniam, quis nostrud exercitation ullamco laboris nisi ut aliquip ex ea commodo consequat. Duis aute irure dolor</p>
  <p class="abs lender-copy" style="top:1819px">Lorem ipsum dolor sit amet, consectetur adipiscing elit, sed do eiusmod tempor incididunt ut labore et dolore magna aliqua. Ut enim ad minim veniam, quis nostrud exercitation ullamco laboris nisi ut aliquip ex ea commodo consequat. Duis aute irure dolor</p>
  <span class="abs btn-light" style="left:854px;top:1956px;width:153px;height:35px;line-height:33px;font-weight:400">Private Lender Alert</span>

  <footer class="abs footer"></footer>
  <div class="abs footer-head" style="left:101px">SOLUTIONS</div>
  <ul class="abs footer-list" style="left:101px"><li>Fast Cash</li><li>Normal Sale</li><li>Short Settlement</li><li>Long Settlement</li><li>Profit Sharing</li><li>Sell the Debt / Keep the Income</li></ul>
  <div class="abs footer-head" style="left:352px">QUICK LINKS</div>
  <ul class="abs footer-list" style="left:352px"><li>Home</li><li>About us</li><li>Our Services</li><li>Our Projects</li><li>Meet our Team</li><li>Contact us</li></ul>
  <div class="abs footer-head" style="left:546px">SIGN UP FOR NEWSLETTER</div>
  <p class="abs news-copy">Excepteur sint occaecat cupidatat non dent, sunt in culpa qui officia</p>
  <div class="abs news-input">Enter Name</div>
  <div class="abs news-btn">SUBSCRIBE</div>
  <div class="abs footer-head" style="left:850px">CONTACT US</div>
  <div class="abs footer-contact">PO Box 218<br>HOLLOWAY PLAINS Qld 4309</div>
  <div class="abs footer-row" style="top:2199px"><svg width="16" height="16" viewBox="0 0 24 24"><path d="M6.6 10.8a15.1 15.1 0 0 0 6.6 6.6l2.2-2.2c.3-.3.7-.4 1-.2 1.1.4 2.3.6 3.6.6.6 0 1 .4 1 1V20c0 .6-.4 1-1 1A17 17 0 0 1 3 4c0-.6.4-1 1-1h3.5c.6 0 1 .4 1 1 0 1.3.2 2.5.6 3.6.1.3 0 .7-.2 1z" fill="none" stroke="#fff" stroke-width="1.6"/></svg>+1800 555 318</div>
  <div class="abs footer-row" style="top:2230px"><svg width="16" height="12" viewBox="0 0 16 12"><rect x="1" y="1" width="14" height="10" fill="none" stroke="#fff" stroke-width="1.3"/><path d="M1 1l7 6 7-6" fill="none" stroke="#fff" stroke-width="1.3"/></svg>info@tarnvalepropertyco.com.au</div>
  <span class="abs social" style="left:855px"></span>
  <span class="abs social" style="left:884px"></span>
  <span class="abs social" style="left:913px"></span>
  <span class="abs social" style="left:942px"></span>
  <span class="abs social" style="left:971px"></span>
  <div class="abs footer-bar">©2014 - 2015  TARNVALE PROPERTY CO (AUST.) PTY LTD., All Rights Reserved.</div>

</div>
</body>
</html>
```